Dunkerfell - Large Clipvale Channel needs Website (3 million subscribers)

Dunkerfell is a clipvale channel that specialises in violent action/comedy/horror skits. We currently have over 3 million subscirbers.

We are looking to have a website created mainly to act as a gateway to our merchandise.

We want it to be simple and easy to use.

Attached is a copy of our Logo which the website can be based off.

Also Attached is some Images of our shirts and Hats.

I believe we'd need a Home page, product page, contact page and a checkout cart page.

Here is a link to our Clipvale channel - https://www.clipvale-hub.net/channel/QHm_pLx_7wrNEo3TbkZgMa9s

Clipvale

Coded - Design and coding required

```html
<!DOCTYPE html>
<html lang="en">
<head>
<meta charset="utf-8">
<title>Dunkerfell Official Merch Store</title>
<link href="https://fonts.googleapis.com/css2?family=Montserrat:ital,wght@0,300;0,400;0,500;0,600;0,700;1,400&display=swap" rel="stylesheet">
<style>
:root{
  --red:#cc1f24;
  --red-mid:#b81b21;
  --red-dark:#a8171c;
  --ink:#1d1d1d;
  --body:#333333;
  --muted:#6f6f6f;
  --light:#e8e7e6;
  --footer:#231f20;
  --footer-line:#3a3536;
  --footer-text:#d8d8d8;
  --white:#ffffff;
}
*{box-sizing:border-box;margin:0;padding:0}
html,body{width:1200px;height:2889px;overflow:hidden}
body{position:relative;background:var(--white);font-family:'Montserrat',sans-serif;color:var(--ink)}
.abs{position:absolute}
a{color:inherit;text-decoration:none}

/* hero */
.hero{left:0;top:0;width:1200px;height:549px;background:radial-gradient(ellipse at 40% 45%,#3b3a36 0%,#1e1d1b 55%,#0e0e0d 100%)}
.brand{left:208px;top:58px;display:flex;align-items:center;gap:10px;color:var(--white);font-weight:700;font-size:26px;letter-spacing:.5px}
.brand-dot{width:16px;height:16px;border-radius:50%;background:var(--red)}
.nav{top:70px;left:0;height:20px;color:var(--white);font-size:10px;font-weight:500;letter-spacing:1px;text-transform:uppercase}
.nav-item{position:absolute;top:3px;white-space:nowrap}
.nav-btn{position:absolute;top:-3px;height:24px;border:1.5px solid var(--white);border-radius:12px;font-size:9.5px;display:flex;align-items:center;justify-content:center;white-space:nowrap}
.hero-kicker{top:227px;width:1200px;text-align:center;color:var(--white);font-size:13px;font-weight:500;letter-spacing:1.5px}
.hero-title{top:252px;width:1200px;text-align:center;color:var(--white);font-size:36px;font-weight:300;line-height:1.2}
.hero-sub{top:300px;width:1200px;text-align:center;color:var(--white);font-size:13px}
.hero-btn{left:531px;top:343px;width:138px;height:29px;border:2px solid var(--white);border-radius:15px;color:var(--white);font-size:10px;font-weight:600;letter-spacing:1px;display:flex;align-items:center;justify-content:center}
.hero-arrow{top:277px}

/* feature strip */
.strip-shadow{left:179px;top:549px;width:842px;height:81px;background:linear-gradient(#d9d9d9,#ececec);clip-path:polygon(0 0,100% 0,96.5% 100%,3.5% 100%)}
.strip{left:208px;top:493px;width:784px;height:137px;display:flex}
.strip-box{flex:1;display:flex;flex-direction:column;align-items:center;justify-content:center;color:var(--white);font-size:12.5px;font-weight:600;text-align:center;line-height:1.35;gap:10px}
.strip-box:nth-child(1){background:var(--red)}
.strip-box:nth-child(2){background:var(--red-mid)}
.strip-box:nth-child(3){background:var(--red-dark)}
.strip-mark{font-weight:700;font-size:12.5px;height:36px;display:flex;align-items:center}

/* section titles */
.section-title{width:1200px;text-align:center;font-size:20px;font-weight:600;letter-spacing:.5px;text-transform:uppercase}

/* about */
.about-photo{left:0;top:732px;width:603px;height:343px;background:linear-gradient(180deg,#b7b2aa 0%,#6d6862 55%,#2f2e30 100%)}
.about-panel{left:603px;top:732px;width:597px;height:343px;background:var(--light)}
.about-title{left:643px;top:770px;font-size:16px;font-weight:500}
.about-lead{left:643px;top:805px;width:345px;font-size:12.5px;line-height:1.38;color:var(--body)}
.about-body{left:643px;top:888px;width:345px;font-size:10px;line-height:1.5;color:var(--muted)}
.pill{background:var(--red);color:var(--white);border-radius:14px;font-size:9.5px;font-weight:600;letter-spacing:1px;display:flex;align-items:center;justify-content:center;text-transform:uppercase;white-space:nowrap}

/* collections */
.collection{top:1175px;width:248px;height:323px;display:flex;flex-direction:column;align-items:center;justify-content:center;color:var(--white);text-align:center}
.collection-name{font-size:17px;font-weight:500}
.collection-text{font-size:10.5px;line-height:1.4;width:180px;margin-top:8px;font-style:italic}

/* popular */
.thumb{top:1599px;width:181px;height:177px}
.thumb-meta{top:1795px;width:195px}
.by{font-size:8px;font-weight:600;letter-spacing:.5px}
.item-title{font-size:12.5px;font-weight:600;margin-top:5px;white-space:nowrap}
.item-info{font-size:9px;color:var(--muted);margin-top:3px}
.price{display:flex;align-items:center;gap:8px;color:var(--white);font-weight:600;font-size:13.5px}

/* featured */
.tile{display:flex;flex-direction:column;align-items:center;justify-content:center;color:var(--white);text-align:center}
.tile-title{font-size:12.5px;font-weight:600;margin-top:8px}
.tile-info{font-size:9.5px;margin-top:2px}
.tile .price{margin-top:8px}

/* contact cta */
.cta-title{top:2488px;width:1200px;text-align:center;color:var(--red);font-size:33px;font-weight:400}
.cta-text{top:2533px;width:1200px;text-align:center;font-size:12.5px;line-height:1.55}
.cta-btn{left:537px;top:2594px;width:126px;height:29px;border:2px solid var(--red);border-radius:15px;color:var(--red);font-size:10px;font-weight:600;letter-spacing:1px;display:flex;align-items:center;justify-content:center}

/* footer */
.footer{left:0;top:2668px;width:1200px;height:221px;background:var(--footer);color:var(--footer-text)}
.foot-col{top:38px}
.foot-head{font-size:9.5px;font-weight:700;letter-spacing:1px;color:var(--white);margin-bottom:6px}
.foot-link{font-size:10px;line-height:19px}
.foot-link.active{color:var(--red)}
.foot-rule{left:0;top:155px;width:1200px;height:1px;background:var(--footer-line)}
.foot-legal{left:208px;top:183px;font-size:9.5px;display:flex;gap:22px}
.foot-legal .hl{color:var(--red)}
.socials{left:902px;top:179px;display:flex;gap:6px}
.social{width:16px;height:16px;border:1.5px solid #cfcfcf;border-radius:50%}
.social.first{border-color:var(--red)}
</style>
</head>
<body>

<!-- HERO -->
<section class="hero abs" role="img" aria-label="Dark cinematic action scene with a figure in a misty forest"></section>
<div class="brand abs"><span class="brand-dot"></span>Dunkerfell</div>
<nav class="nav abs">
  <a class="nav-item" style="left:424px">About us</a>
  <a class="nav-item" style="left:516px">Shop ⌄</a>
  <a class="nav-item" style="left:601px">Contact</a>
  <svg class="nav-item" style="left:709px;top:2px" width="13" height="13" viewBox="0 0 14 14"><circle cx="6" cy="6" r="4.5" fill="none" stroke="#fff" stroke-width="2"/><line x1="9.3" y1="9.3" x2="13" y2="13" stroke="#fff" stroke-width="2"/></svg>
  <a class="nav-btn" style="left:751px;width:60px">Login</a>
  <a class="nav-btn" style="left:822px;width:83px">Register</a>
  <a class="nav-btn" style="left:915px;width:75px">Cart (0)</a>
</nav>
<div class="hero-kicker abs">OFFICIAL MERCH</div>
<h1 class="hero-title abs">Shop Dunkerfell Shirts &amp; Hats</h1>
<p class="hero-sub abs">Wear the skits you love, printed in limited runs</p>
<a class="hero-btn abs">SHOP NOW</a>
<svg class="hero-arrow abs" style="left:134px" width="24" height="44" viewBox="0 0 24 44"><polyline points="22,2 3,22 22,42" fill="none" stroke="#fff" stroke-width="2.5"/></svg>
<svg class="hero-arrow abs" style="left:1042px" width="24" height="44" viewBox="0 0 24 44"><polyline points="2,2 21,22 2,42" fill="none" stroke="#cc1f24" stroke-width="2.5"/></svg>

<!-- FEATURE STRIP -->
<div class="strip-shadow abs"></div>
<div class="strip abs">
  <div class="strip-box"><span class="strip-mark">Dunkerfell</span>Official Channel<br>Merchandise</div>
  <div class="strip-box"><svg width="36" height="36" viewBox="0 0 36 36"><circle cx="18" cy="18" r="16" fill="none" stroke="#fff" stroke-width="2"/><path d="M10 12h3l2.5 9h9l2-6.5H14" fill="none" stroke="#fff" stroke-width="2"/><circle cx="16" cy="25" r="1.5" fill="#fff"/><circle cx="23" cy="25" r="1.5" fill="#fff"/></svg>Purchase High-quality<br>Shirts</div>
  <div class="strip-box"><svg width="36" height="36" viewBox="0 0 36 36"><circle cx="18" cy="18" r="16" fill="none" stroke="#fff" stroke-width="2"/><path d="M11 18a7 7 0 0 1 12-5M25 18a7 7 0 0 1-12 5" fill="none" stroke="#fff" stroke-width="2"/></svg>24X7 Support &amp;<br>Easy Returns</div>
</div>

<!-- ABOUT -->
<h2 class="section-title abs" style="top:668px">About us</h2>
<div class="about-photo abs" role="img" aria-label="Group photo of the channel team"></div>
<div class="about-panel abs"></div>
<h3 class="about-title abs">Dunkerfell Merch Store</h3>
<p class="about-lead abs">Our official store brings the channel's action, comedy and horror skits to shirts and hats, shipped to fans around the globe.</p>
<p class="about-body abs">Every design is drawn from our favourite skits and printed in small runs on soft, durable cotton. Pick a product, choose your size, add it to your cart and check out in a few steps. Questions about sizing or delivery? Our contact page is always open.</p>
<a class="pill abs" style="left:643px;top:1003px;width:127px;height:28px">View details</a>

<!-- COLLECTIONS -->
<h2 class="section-title abs" style="top:1110px">Our collections</h2>
<div class="collection abs" style="left:208px;background:linear-gradient(#3a3532,#1c1a19)" role="img" aria-label="Violent action collection image">
  <div class="collection-name">Violent Action</div>
  <div class="collection-text">Shirts and hats inspired by our hardest hitting action skits.</div>
  <a class="pill" style="width:140px;height:28px;margin-top:14px">View collection</a>
</div>
<div class="collection abs" style="left:476px;background:linear-gradient(160deg,#b9a23a 0%,#4f7a3a 45%,#c26a1e 100%)" role="img" aria-label="Comedy collection image">
  <div class="collection-name">Comedy</div>
</div>
<div class="collection abs" style="left:745px;background:linear-gradient(#2e3a30,#4b4b3f 60%,#1d1f1b)" role="img" aria-label="Horror skits collection image">
  <div class="collection-name">Horror Skits</div>
</div>

<!-- POPULAR -->
<h2 class="section-title abs" style="top:1535px">Popular products</h2>
<svg class="abs" style="left:143px;top:1686px" width="14" height="28" viewBox="0 0 14 28"><polyline points="13,1 2,14 13,27" fill="none" stroke="#aaa" stroke-width="2"/></svg>
<svg class="abs" style="left:1043px;top:1686px" width="14" height="28" viewBox="0 0 14 28"><polyline points="1,1 12,14 1,27" fill="none" stroke="#cc1f24" stroke-width="2"/></svg>

<div class="thumb abs" style="left:208px;background:#1e1e1e" role="img" aria-label="Zombie print t-shirt">
  <a class="pill abs" style="left:28px;top:76px;width:126px;height:27px">Add to cart</a>
  <div class="price abs" style="left:52px;top:138px"><svg width="18" height="15" viewBox="0 0 18 15"><path d="M1 1.5h3l2 8h9l2-6H5" fill="none" stroke="#fff" stroke-width="1.8"/><circle cx="7.5" cy="13" r="1.4" fill="#fff"/><circle cx="14" cy="13" r="1.4" fill="#fff"/></svg>$25.00</div>
</div>
<div class="thumb abs" style="left:410px;background:linear-gradient(#e5e5e5,#3d3d3d)" role="img" aria-label="Black and white circus skit snapback hat"></div>
<div class="thumb abs" style="left:611px;background:linear-gradient(#3f4a3e,#1a2018)" role="img" aria-label="Gaming parody hoodie"></div>
<div class="thumb abs" style="left:811px;background:linear-gradient(#b9b3a8,#5b5954)" role="img" aria-label="Chicken suit skit cap"></div>

<div class="thumb-meta abs" style="left:208px"><div class="by">BY DUNKERFELL</div><div class="item-title">Zombie Logo Tee (1979)</div><div class="item-info">T-shirt / 410 sold</div></div>
<div class="thumb-meta abs" style="left:410px"><div class="by">BY DUNKERFELL</div><div class="item-title">Circus Skit Snapback</div><div class="item-info">Hat / 4100 sold</div></div>
<div class="thumb-meta abs" style="left:611px"><div class="by">BY DUNKERFELL</div><div class="item-title">Frontline Duty Hoodie</div><div class="item-info">Hoodie / 4100 sold</div></div>
<div class="thumb-meta abs" style="left:811px"><div class="by">BY DUNKERFELL</div><div class="item-title">Chicken Suit Cap</div><div class="item-info">Hat / 20,000 sold</div></div>

<!-- FEATURED -->
<h2 class="section-title abs" style="top:1877px">Featured merch</h2>
<div class="tile abs" style="left:0;top:1941px;width:589px;height:515px;background:radial-gradient(ellipse at 45% 50%,#566166 0%,#2b3034 55%,#15181a 100%)" role="img" aria-label="Action fight print shirt">
  <svg width="36" height="36" viewBox="0 0 36 36"><circle cx="18" cy="18" r="16" fill="none" stroke="#fff" stroke-width="2"/><path d="M11 12h3l2.5 9h9l2-6.5H15" fill="none" stroke="#fff" stroke-width="2"/><circle cx="17" cy="25" r="1.5" fill="#fff"/><circle cx="24" cy="25" r="1.5" fill="#fff"/></svg>
  <div class="tile-title">Zombie Full Print Tee (1979)</div><div class="tile-info">T-shirt / S – XXL</div>
  <div class="price">$25.00</div>
</div>
<div class="tile abs" style="left:611px;top:1941px;width:283px;height:245px;background:linear-gradient(#5a4a3e,#2a2320)" role="img" aria-label="Comedy skit shirt">
  <svg width="36" height="36" viewBox="0 0 36 36"><circle cx="18" cy="18" r="16" fill="none" stroke="#fff" stroke-width="2"/><path d="M11 12h3l2.5 9h9l2-6.5H15" fill="none" stroke="#fff" stroke-width="2"/><circle cx="17" cy="25" r="1.5" fill="#fff"/><circle cx="24" cy="25" r="1.5" fill="#fff"/></svg>
  <div class="tile-title">Comedy Skit Shirt (2016)</div><div class="tile-info">T-shirt / 4410 sold</div>
  <div class="price">$25.00</div>
</div>
<div class="tile abs" style="left:917px;top:1941px;width:283px;height:245px;background:linear-gradient(135deg,#7a3426,#2c1813)" role="img" aria-label="Selfie skit hat">
  <svg width="36" height="36" viewBox="0 0 36 36"><circle cx="18" cy="18" r="16" fill="none" stroke="#fff" stroke-width="2"/><path d="M11 12h3l2.5 9h9l2-6.5H15" fill="none" stroke="#fff" stroke-width="2"/><circle cx="17" cy="25" r="1.5" fill="#fff"/><circle cx="24" cy="25" r="1.5" fill="#fff"/></svg>
  <div class="tile-title">Selfy Crew Hat</div><div class="tile-info">Hat / 41,000 sold</div>
  <div class="price">$18.00</div>
</div>
<div class="tile abs" style="left:611px;top:2211px;width:283px;height:245px;background:linear-gradient(#4b3a34,#1f1816)" role="img" aria-label="Horror zombie hoodie">
  <svg width="36" height="36" viewBox="0 0 36 36"><circle cx="18" cy="18" r="16" fill="none" stroke="#fff" stroke-width="2"/><path d="M11 12h3l2.5 9h9l2-6.5H15" fill="none" stroke="#fff" stroke-width="2"/><circle cx="17" cy="25" r="1.5" fill="#fff"/><circle cx="24" cy="25" r="1.5" fill="#fff"/></svg>
  <div class="tile-title">Horror Zombia Hoodie</div><div class="tile-info">Hoodie / 20,000 sold</div>
  <div class="price">$45.00</div>
</div>
<div class="tile abs" style="left:917px;top:2211px;width:283px;height:245px;background:linear-gradient(135deg,#284447,#121a1b)" role="img" aria-label="Violent action cap">
  <svg width="36" height="36" viewBox="0 0 36 36"><circle cx="18" cy="18" r="16" fill="none" stroke="#fff" stroke-width="2"/><path d="M11 12h3l2.5 9h9l2-6.5H15" fill="none" stroke="#fff" stroke-width="2"/><circle cx="17" cy="25" r="1.5" fill="#fff"/><circle cx="24" cy="25" r="1.5" fill="#fff"/></svg>
  <div class="tile-title">Violent Action Cap</div><div class="tile-info">Hat / 410 sold</div>
  <div class="price">$20.00</div>
</div>

<!-- CONTACT CTA -->
<h2 class="cta-title abs">Got a Question?</h2>
<p class="cta-text abs">Reach our team about orders, sizing and shipping for every Dunkerfell shirt and hat.<br>The best part? We reply to every message within one business day.</p>
<a class="cta-btn abs">CONTACT US</a>

<!-- FOOTER -->
<footer class="footer abs">
  <div class="foot-col abs" style="left:208px"><div class="foot-head">SHOP</div><div class="foot-link active">Home</div><div class="foot-link">Shirts</div><div class="foot-link">Hats</div><div class="foot-link">Browse All</div></div>
  <div class="foot-col abs" style="left:410px"><div class="foot-head">CUSTOMERS</div><div class="foot-link">Join</div><div class="foot-link">Log In</div><div class="foot-link">Cart</div><div class="foot-link">Checkout</div></div>
  <div class="foot-col abs" style="left:611px"><div class="foot-head">CONTACT</div><div class="foot-link">Contact Us</div><div class="foot-link">Clipvale Channel</div></div>
  <div class="foot-col abs" style="left:811px"><div class="foot-head">HELP</div><div class="foot-link">Ordering FAQ</div><div class="foot-link">Shipping FAQ</div><div class="foot-link">Returns FAQ</div><div class="foot-link">Help Center</div></div>
  <div class="foot-rule abs"></div>
  <div class="foot-legal abs"><span>TM + © 2017 <span class="hl">Dunkerfell</span>, Inc. All rights reserved.</span><span>Terms</span><span>Privacy</span><span>Cookies</span></div>
  <div class="socials abs"><span class="social first"></span><span class="social"></span><span class="social"></span><span class="social"></span></div>
  <svg class="abs" style="left:996px;top:174px" width="26" height="26" viewBox="0 0 26 26"><circle cx="13" cy="13" r="11.5" fill="none" stroke="#cc1f24" stroke-width="2"/><path d="M13 19V9M8.5 13.5L13 9l4.5 4.5M8.5 7h9" fill="none" stroke="#cc1f24" stroke-width="2"/></svg>
</footer>

</body>
</html>
```